Letterhead Design Project

We have recently updated our corporate logo and are seeking a new letterhead template.

Attached is the new logo and the old letterhead.

PLEASE DO NOT USE OUR EXISTING WEB SITE FOR INSPIRATION as we are redesigning it.

Target Market(s)

Executives, search professionals, technical and scientific professionals

Industry/Entity Type

Seeking

```html
<!DOCTYPE html>
<html lang="en">
<head>
<meta charset="utf-8">
<title>HelixSeek Letterhead</title>
<link href="https://fonts.googleapis.com/css2?family=Nunito:wght@600&family=Noto+Sans:wght@400;700&display=swap" rel="stylesheet">
<style>
  :root {
    --backdrop: #ffffff;
    --paper: #ffffff;
    --paper-edge: #8a8a8a;
    --band: #f3f4f4;
    --band-line: #e6e8e8;
    --brand-blue: #1a8fd0;
    --ink: #1a1a1a;
    --slate: #4a5556;
    --helix-light: #e8f4fa;
    --helix-mid: #7cc6ea;
    --helix-deep: #2f8fc4;
  }
  * { margin: 0; padding: 0; box-sizing: border-box; }
  html, body {
    width: 1200px; height: 920px; overflow: hidden;
    background: var(--backdrop);
  }
  .letterhead {
    position: absolute;
    left: 293px; top: 63px;
    width: 617px; height: 798px;
    background: var(--paper);
    border: 1px solid var(--paper-edge);
    box-shadow: 1px 2px 3px rgba(0,0,0,0.35);
    overflow: hidden;
  }
  .header-band {
    position: absolute;
    left: 0; top: 20px;
    width: 100%; height: 63px;
    background: var(--band);
    border-top: 3px solid var(--band-line);
    border-bottom: 3px solid var(--band-line);
  }
  .header-art {
    position: absolute;
    left: 0; top: 0;
    width: 157px; height: 112px;
    background:
      radial-gradient(ellipse at 40% 45%, var(--helix-mid) 0%, var(--helix-deep) 35%, rgba(124,198,234,0.35) 65%, rgba(255,255,255,0) 85%),
      linear-gradient(135deg, #9aa5ab 0%, var(--helix-light) 70%, #ffffff 100%);
    opacity: 0.85;
  }
  .brand {
    position: absolute;
    left: 35px; top: 37px;
    display: flex; align-items: center; gap: 6px;
  }
  .brand-dot {
    width: 30px; height: 30px; border-radius: 50%;
    background: var(--brand-blue);
  }
  .brand-name {
    font-family: "Nunito", sans-serif;
    font-weight: 600;
    font-size: 27px;
    letter-spacing: -0.3px;
    color: var(--brand-blue);
    line-height: 1;
  }
  .contact {
    position: absolute;
    right: 15px; top: 28px;
    text-align: right;
    font-family: "Noto Sans", sans-serif;
    font-size: 9.5px;
    line-height: 12.2px;
    color: var(--ink);
    list-style: none;
    letter-spacing: 0.2px;
  }
  .footer-web {
    position: absolute;
    left: 0; right: 0; top: 748px;
    text-align: center;
    font-family: "Noto Sans", sans-serif;
    font-weight: 700;
    font-size: 13.5px;
    color: var(--ink);
  }
</style>
</head>
<body>
  <main class="letterhead">
    <div class="header-band"></div>
    <div class="header-art" role="img" aria-label="Soft blue DNA helix imagery fading into the page corner"></div>
    <div class="brand">
      <span class="brand-dot"></span>
      <span class="brand-name">HelixSeek</span>
    </div>
    <ul class="contact">
      <li>Voice: 555-201-0100</li>
      <li>Fax: 555-201-0110</li>
      <li>420 Ridgeline Avenue, Suite 310</li>
      <li>Easton Falls, MA 02399</li>
    </ul>
    <p class="footer-web">www.HelixSeek.com</p>
  </main>
</body>
</html>
```